Business Card Design Project

for a second hand vintage clothing store. shop name is The Velvet Cupboard

Cards to be double sided

The name on the card is Joanna Whitfield

Information to put on card:

The Velvet Cupboard
Joanna Whitfield (no job title)
42/871 Dunmore St, Glenwick, Sydney, NSW, 2009.
Mobile: 0412 905 261
Email: thevelvetcupboard@mailbox.com.au
Web: www.thevelvetcupboard.com.au

Target Market(s)

Women looking at vintage clothing

Industry/Entity Type

Clothing

```html
<!DOCTYPE html>
<html lang="en">
<head>
<meta charset="utf-8">
<title>The Velvet Cupboard — Business Card</title>
<link rel="stylesheet" href="https://fonts.googleapis.com/css2?family=Tinos&display=swap">
<style>
  :root {
    --backdrop: #97a2a8;
    --plum: #451234;
    --ink-plum: #3d1033;
    --paper: #ffffff;
    --gold: #ede08a;
    --orange: #e8852a;
    --card-shadow: 5px 6px 5px rgba(20, 20, 25, 0.75);
  }
  * { margin: 0; padding: 0; box-sizing: border-box; }
  html, body {
    width: 1200px;
    height: 900px;
    overflow: hidden;
    background: var(--backdrop);
    font-family: "Tinos", "Times New Roman", serif;
  }
  .canvas {
    position: relative;
    width: 1200px;
    height: 900px;
  }
  .card {
    position: absolute;
    left: 335px;
    width: 539px;
    box-shadow: var(--card-shadow);
  }
  .card--front {
    top: 60px;
    height: 372px;
    background: var(--plum);
  }
  .card--back {
    top: 460px;
    height: 370px;
    background: var(--paper);
  }
  .brand {
    position: absolute;
    display: flex;
    align-items: center;
    white-space: nowrap;
  }
  .brand-mark {
    flex: none;
    border-radius: 50%;
    background: var(--orange);
  }
  .brand-name {
    font-weight: 400;
    line-height: 1;
  }
  .card--front .brand {
    left: 53px;
    top: 254px;
    gap: 12px;
  }
  .card--front .brand-mark { width: 14px; height: 14px; }
  .card--front .brand-name {
    font-size: 40px;
    color: var(--gold);
  }
  .card--back .brand {
    left: 48px;
    top: 62px;
    gap: 9px;
  }
  .card--back .brand-mark { width: 11px; height: 11px; }
  .card--back .brand-name {
    font-size: 30px;
    color: var(--ink-plum);
  }
  .contact {
    position: absolute;
    left: 46px;
    top: 193px;
    list-style: none;
    font-size: 21px;
    line-height: 27px;
    color: var(--ink-plum);
  }
  .accent { color: var(--orange); }
</style>
</head>
<body>
<main class="canvas">
  <section class="card card--front" aria-label="Card front">
    <div class="brand">
      <span class="brand-mark" aria-hidden="true"></span>
      <span class="brand-name">The Velvet Cupboard</span>
    </div>
  </section>

  <section class="card card--back" aria-label="Card back">
    <div class="brand">
      <span class="brand-mark" aria-hidden="true"></span>
      <span class="brand-name">The Velvet Cupboard</span>
    </div>
    <ul class="contact">
      <li class="accent">Joanna Whitfield</li>
      <li>42/871 Dunmore St, Glenwick, Sydney, NSW, 2009</li>
      <li><span class="accent">Mob</span> 0412 905 261</li>
      <li>thevelvetcupboard<span class="accent">@</span>mailbox.com.au</li>
      <li>www.<span class="accent">thevelvetcupboard</span>.com.au</li>
    </ul>
  </section>
</main>
</body>
</html>
```